International PR and marketing agency needs website design

We need a branding website, for a company based in the US (Washington DC). We are a communication (PR, marketing, social media) agency. We already have the copy, and we have some example websites (some major agencies), that we like.
For example:
https://pellowtrask.example/
https://durnevaleglobal.example/
https://varnok.example/
https://qmf-reach.example/
https://www.thornbury.example/
The website must be a multi-language site, we will add the new languages step-by-step.
We would like to upload content continuously.
The website has to have sub-pages (segments), and news part.
Target Market(s)
Global
Industry/Entity Type
Public relations, Communications, Marketing, Social Media
Number of Pages Required
5+ page
Font styles to use
Other font styles liked:
- Well readable, modern style.
Look and feel

```html
<!DOCTYPE html>
<html lang="en">
<head>
<meta charset="utf-8">
<title>Meridian PR — Building Relationships</title>
<link href="https://fonts.googleapis.com/css2?family=Plus+Jakarta+Sans:wght@400;500;600;700;800&display=swap" rel="stylesheet">
<style>
:root{
  --red:#e3101f;
  --purple:#8e2a85;
  --navy:#101a3a;
  --text:#3a3f4f;
  --muted:#6b7080;
  --tint:#f8f8fd;
  --white:#ffffff;
  --grad:linear-gradient(90deg,var(--red),var(--purple));
}
*{margin:0;padding:0;box-sizing:border-box}
html,body{width:1200px;height:3448px;overflow:hidden}
body{position:relative;background:var(--white);font-family:"Plus Jakarta Sans",Arial,sans-serif;color:var(--text)}
a{color:inherit;text-decoration:none}
.abs{position:absolute}

/* hero */
.hero{position:absolute;left:0;top:0;width:1200px;height:614px;clip-path:polygon(0 0,100% 0,100% 489px,0 614px);overflow:hidden}
.hero-photo{position:absolute;inset:0;background:linear-gradient(100deg,#3a3f48 0%,#6f7a88 45%,#9aa4b2 70%,#4b5666 100%)}
.hero-shade{position:absolute;inset:0;background:linear-gradient(90deg,rgba(8,8,10,.95) 0%,rgba(8,8,10,.8) 30%,rgba(8,8,10,.2) 55%,rgba(8,8,10,0) 75%)}
.brand{position:absolute;display:flex;align-items:center;gap:8px;font-weight:800;color:var(--red);font-size:24px;letter-spacing:-.5px}
.brand-dot{width:22px;height:22px;border-radius:50%;background:var(--red)}
.nav{position:absolute;top:30px;left:447px;display:flex;gap:0;font-size:10px;font-weight:600;color:var(--white);letter-spacing:.2px}
.nav a{position:absolute;white-space:nowrap;display:flex;align-items:center;gap:5px}
.flag{display:inline-block;width:14px;height:9px;background:linear-gradient(#c8102e 0 50%,#fff 50%);border-radius:1px}
.hero-kicker{left:163px;top:158px;font-size:33px;font-weight:400;color:var(--white)}
.hero-title{left:163px;top:196px;font-size:60px;font-weight:800;color:var(--white);letter-spacing:.5px}
.hero-sub{left:163px;top:258px;font-size:42px;font-weight:400;color:var(--white);letter-spacing:.3px}
.hero-text{left:163px;top:327px;width:340px;font-size:15.5px;line-height:24px;color:var(--white)}
.btn{position:absolute;display:flex;align-items:center;justify-content:space-between;padding:0 20px 0 22px;height:37px;border-radius:19px;background:var(--grad);color:var(--white);font-size:9.5px;font-weight:700;box-shadow:0 6px 14px rgba(227,16,31,.22)}
.btn svg{width:8px;height:8px}

/* who we are */
.eyebrow{position:absolute;left:0;width:1200px;text-align:center;font-size:17px;font-weight:700;letter-spacing:3.5px;color:var(--red)}
.who-lead{left:300px;width:600px;top:684px;text-align:center;font-size:17px;line-height:26px;color:var(--navy)}
.who-quote{left:340px;width:520px;top:747px;text-align:center;font-size:11.5px;line-height:20px;color:var(--text)}

/* expertise */
.expertise-bg{position:absolute;left:0;top:938px;width:1200px;height:1440px;background:var(--tint);clip-path:polygon(0 0,100% 0,100% 1298px,0 1440px)}
.pill{position:absolute;height:52px;border-radius:26px;border:1px solid #eceef6;background:rgba(255,255,255,.5)}
.pill.pink{background:#fbf1f4;border-color:#fbf1f4}
.photo{position:absolute;border-radius:12px;overflow:hidden}
.ph-practices{left:244px;top:1067px;width:300px;height:313px;background:linear-gradient(135deg,#e9ecf0,#b9c2cf 60%,#8f9bb0)}
.ph-esport{left:656px;top:1462px;width:300px;height:313px;background:linear-gradient(135deg,#e7e8ea,#9da3ad 55%,#5c6270)}
.ph-influencers{left:244px;top:1857px;width:300px;height:313px;background:linear-gradient(135deg,#dfe3e8,#8e99aa 50%,#4d5668)}
.exp-title{font-size:34px;font-weight:700;color:var(--navy)}
.exp-text{width:320px;font-size:11.5px;line-height:20.3px;color:var(--text)}

/* news */
.card{position:absolute;top:2429px;width:269px}
.card-img{height:187px;border-radius:12px}
.card-date{margin-top:18px;display:flex;align-items:center;gap:6px;font-size:9.5px;color:var(--muted)}
.card-title{margin-top:12px;font-size:15px;font-weight:700;color:var(--navy)}
.card-text{margin-top:6px;font-size:11.5px;line-height:20px;color:var(--text)}
.card-link{display:inline-block;margin-top:12px;font-size:8px;font-weight:700;color:var(--red);padding-bottom:3px;border-bottom:1px solid var(--red)}

/* cta */
.cta{position:absolute;left:0;top:2812px;width:1200px;height:448px;background:linear-gradient(100deg,var(--red) 0%,#c8143a 40%,var(--purple) 100%);clip-path:polygon(0 0,100% 120px,100% 448px,0 321px)}
.cta-title{left:0;width:1200px;top:2962px;text-align:center;font-size:34px;font-weight:700;color:var(--white)}
.cta-text{left:340px;width:520px;top:3017px;text-align:center;font-size:11.5px;line-height:20px;color:var(--white)}
.btn-outline{background:transparent;border:1.5px solid var(--white);box-shadow:none}

/* footer */
.foot-link{left:244px;font-size:9.5px;font-weight:700;color:var(--navy)}
.foot-label{display:flex;align-items:center;gap:6px;font-size:10.5px;font-weight:600;color:var(--navy)}
.foot-val{margin-top:5px;font-size:10.5px;line-height:15px;color:var(--muted)}
.foot-big{margin-top:4px;font-size:14px;color:var(--muted)}
.socials{position:absolute;left:811px;top:3369px;display:flex;gap:9px}
.socials span{width:23px;height:23px;border-radius:50%;border:1px solid #c9ccd6}
.copy{left:844px;top:3414px;font-size:8px;color:#a0a4b0}
</style>
</head>
<body>

<header class="hero">
  <div class="hero-photo" role="img" aria-label="Photo of three smiling colleagues working together around a laptop"></div>
  <div class="hero-shade"></div>
</header>

<div class="brand" style="left:167px;top:24px"><span class="brand-dot"></span>Meridian PR</div>

<nav class="nav" aria-label="Main">
  <a style="left:0">WHO WE ARE <svg width="7" height="5" viewBox="0 0 7 5"><path d="M1 1l2.5 2.5L6 1" stroke="#fff" fill="none" stroke-width="1.2"/></svg></a>
  <a style="left:114px">OUR EXPERTIESE <svg width="7" height="5" viewBox="0 0 7 5"><path d="M1 1l2.5 2.5L6 1" stroke="#fff" fill="none" stroke-width="1.2"/></svg></a>
  <a style="left:243px">NEWS</a>
  <a style="left:322px">MERIDIAN LINK</a>
  <a style="left:416px">CONTACT</a>
  <a style="left:516px"><span class="flag"></span> ENGLISH <svg width="7" height="5" viewBox="0 0 7 5"><path d="M1 1l2.5 2.5L6 1" stroke="#fff" fill="none" stroke-width="1.2"/></svg></a>
</nav>

<p class="abs hero-kicker">WE ARE</p>
<h1 class="abs hero-title">BUILDING</h1>
<p class="abs hero-sub">RELATIONSHIPS</p>
<p class="abs hero-text">We understand the needs of our clients, and our experts and our creative staff are working on building long-term relationships.</p>
<a class="btn" style="left:163px;top:433px;width:144px">GET STARTED NOW <svg viewBox="0 0 8 8"><path d="M2.5 1l3 3-3 3" stroke="#fff" fill="none" stroke-width="1.4"/></svg></a>

<section>
  <h2 class="eyebrow" style="top:646px">WHO WE ARE</h2>
  <p class="abs who-lead">we successfully target the key audiences, creating the best marketing strategy, help to build and maintain our clients’ reputations.</p>
  <p class="abs who-quote">“ Meridian PR Solutions is a new kind of communications agency focused on branding, public relations, integrated marketing, social communication, providing full services to our clients. Our business operations are designed to support growth, for our clients. ”</p>
  <a class="btn" style="left:544px;top:827px;width:112px">READ MORE <svg viewBox="0 0 8 8"><path d="M2.5 1l3 3-3 3" stroke="#fff" fill="none" stroke-width="1.4"/></svg></a>
</section>

<section>
  <div class="expertise-bg"></div>
  <div class="pill" style="left:965px;top:1015px;width:158px"></div>
  <div class="pill" style="left:45px;top:1415px;width:160px"></div>
  <div class="pill pink" style="left:-30px;top:1546px;width:160px"></div>
  <div class="pill" style="left:965px;top:1827px;width:158px"></div>
  <h2 class="eyebrow" style="top:1003px">OUR EXPERTISE</h2>

  <div class="photo ph-practices" role="img" aria-label="Photo of a woman presenting charts on a whiteboard"></div>
  <h3 class="abs exp-title" style="left:629px;top:1093px">PRACTICES</h3>
  <p class="abs exp-text" style="left:629px;top:1146px">To make choosing much easier for You, we provide the widest possible range of services. Let it be media relations, crisis management or marketing services, our experts are always available.</p>
  <a class="btn" style="left:628px;top:1256px;width:132px">LEARN MORE <svg viewBox="0 0 8 8"><path d="M2.5 1l3 3-3 3" stroke="#fff" fill="none" stroke-width="1.4"/></svg></a>

  <h3 class="abs exp-title" style="left:245px;top:1488px">eSPORT</h3>
  <p class="abs exp-text" style="left:245px;top:1541px">It is the industry that is developing the fastest, which changes our culture, our relationships to people and the sales strategy of manufacturers in their cores. It is maybe one of the biggest success stories of the 21st century.</p>
  <a class="btn" style="left:244px;top:1649px;width:132px">LEARN MORE <svg viewBox="0 0 8 8"><path d="M2.5 1l3 3-3 3" stroke="#fff" fill="none" stroke-width="1.4"/></svg></a>
  <div class="photo ph-esport" role="img" aria-label="Photo of two business people shaking hands across a desk"></div>

  <div class="photo ph-influencers" role="img" aria-label="Photo of a team joining hands over a laptop"></div>
  <h3 class="abs exp-title" style="left:629px;top:1925px">INFLUENCERS</h3>
  <p class="abs exp-text" style="left:629px;top:1977px">We worked out our program for influencers and clients relying on the expectations towards complex services. As we represent many brands with the natural expectation to work together with the popular.</p>
  <a class="btn" style="left:628px;top:2088px;width:132px">LEARN MORE <svg viewBox="0 0 8 8"><path d="M2.5 1l3 3-3 3" stroke="#fff" fill="none" stroke-width="1.4"/></svg></a>
</section>

<section>
  <h2 class="eyebrow" style="top:2375px">OUR NEWS</h2>
  <div class="pill" style="left:982px;top:2700px;width:158px"></div>
  <div class="pill pink" style="left:1140px;top:2805px;width:120px"></div>

  <article class="card" style="left:163px">
    <div class="card-img" role="img" aria-label="Photo of colleagues in a modern office meeting" style="background:linear-gradient(135deg,#c9d0d8,#7d8796 60%,#4a5262)"></div>
    <div class="card-date"><svg width="10" height="10" viewBox="0 0 10 10"><rect x="1" y="2" width="8" height="7" rx="1" fill="none" stroke="#e3101f"/><path d="M1 4.5h8M3 1v2M7 1v2" stroke="#e3101f"/></svg>Feb 28th, 2023</div>
    <h3 class="card-title">Inspiration</h3>
    <p class="card-text">I resolved, contrary to my first intention, to make the being of a gigantic stature…</p>
    <a class="card-link">LEARN MORE</a>
  </article>
  <article class="card" style="left:466px">
    <div class="card-img" role="img" aria-label="Photo of a man presenting at a flip chart to a seated team" style="background:linear-gradient(135deg,#eef0f2,#b4bcc6 55%,#6e7787)"></div>
    <div class="card-date"><svg width="10" height="10" viewBox="0 0 10 10"><rect x="1" y="2" width="8" height="7" rx="1" fill="none" stroke="#e3101f"/><path d="M1 4.5h8M3 1v2M7 1v2" stroke="#e3101f"/></svg>Nov 15th, 2022</div>
    <h3 class="card-title">The Moments</h3>
    <p class="card-text">I resolved, contrary to my first intention, to make the being of a gigantic stature…</p>
    <a class="card-link">LEARN MORE</a>
  </article>
  <article class="card" style="left:769px">
    <div class="card-img" role="img" aria-label="Photo of a hand signing a document on a desk" style="background:linear-gradient(135deg,#dde2ea,#9aa6b8 55%,#3f4a63)"></div>
    <div class="card-date"><svg width="10" height="10" viewBox="0 0 10 10"><rect x="1" y="2" width="8" height="7" rx="1" fill="none" stroke="#e3101f"/><path d="M1 4.5h8M3 1v2M7 1v2" stroke="#e3101f"/></svg>Nov 3rd, 2022</div>
    <h3 class="card-title">Journey</h3>
    <p class="card-text">I resolved, contrary to my first intention, to make the being of a gigantic stature…</p>
    <a class="card-link">LEARN MORE</a>
  </article>
</section>

<section>
  <div class="cta"></div>
  <h2 class="abs cta-title">Manage Your Investment</h2>
  <p class="abs cta-text">“ Use this line to say something about what you do. Add useful information that your visitors may find interesting. Let your imagination run wild. The possibilities are endless. Get out there and do your thing. ”</p>
  <a class="btn btn-outline" style="left:528px;top:3095px;width:144px;height:40px;border-radius:20px">GET STARTED NOW <svg viewBox="0 0 8 8"><path d="M2.5 1l3 3-3 3" stroke="#fff" fill="none" stroke-width="1.4"/></svg></a>
</section>

<footer>
  <a class="abs foot-link" style="top:3247px">WHO WE ARE</a>
  <a class="abs foot-link" style="top:3287px">OUR EXPERTIS</a>
  <a class="abs foot-link" style="top:3327px">OUR NEWS</a>
  <a class="abs foot-link" style="top:3367px">MERIDIAN LINK</a>
  <a class="abs foot-link" style="top:3407px">CONTACT</a>

  <div class="abs" style="left:465px;top:3245px">
    <div class="foot-label"><svg width="11" height="12" viewBox="0 0 11 12"><path d="M5.5 11S1.5 7 1.5 4.5a4 4 0 018 0C9.5 7 5.5 11 5.5 11z" fill="none" stroke="#e3101f" stroke-width="1.2"/><circle cx="5.5" cy="4.5" r="1.4" fill="#e3101f"/></svg>Address</div>
    <p class="foot-val">2240 Halvern Street NW<br>Washington, District of Columbia<br>20008, US</p>
  </div>
  <div class="abs" style="left:465px;top:3327px">
    <div class="foot-label"><svg width="11" height="11" viewBox="0 0 11 11"><path d="M2 1l2 .3.8 2.2-1.2 1a6 6 0 002.9 2.9l1-1.2 2.2.8.3 2c-.5.6-1.2.9-2 .8C4.5 9.4 1.6 6.5 1.2 3 1.1 2.2 1.4 1.5 2 1z" fill="none" stroke="#e3101f" stroke-width="1.1"/></svg>Phone</div>
    <p class="foot-big">+1 202 555 0148</p>
  </div>
  <div class="abs" style="left:465px;top:3380px">
    <div class="foot-label"><svg width="12" height="10" viewBox="0 0 12 10"><rect x="1" y="1" width="10" height="8" rx="1" fill="none" stroke="#e3101f" stroke-width="1.1"/><path d="M1.5 1.5L6 5.5l4.5-4" fill="none" stroke="#e3101f" stroke-width="1.1"/></svg>Email</div>
    <p class="foot-big">hello@meridianpr.example</p>
  </div>

  <div class="brand" style="left:820px;top:3292px;font-size:24px"><span class="brand-dot"></span>Meridian PR</div>
  <div class="socials" aria-label="Social links"><span></span><span></span><span></span><span></span></div>
  <p class="abs copy">© 2023 Meridian PR</p>
</footer>

</body>
</html>
```